Gutscheine
Zielgruppe
Immobilienmakler, Verkauf und Vermietung, Immobilienbewertung
Aufgabenstellung
Es soll eine Gutscheinkarte werden für die Verteilung auf einen Stadtfest am Stand vor unserem Büro.
Es soll ein Bezug zu Immobilien haben, aber auch eine Emotion vermitteln. Daher Bild mit Familie oder Rentner. Zielgruppe sollen sein zum einen junge Leute, die vor haben eine Immobilie zu kaufen. Und auf der anderen Seite Leute, die mit dem Gedanken spielen eine Immobilie aus Altersgründen, Trennung, Scheidung oder nach Erbe zu verkaufen. Dominant soll mit dem Gutschein zur kostenlosen Bewertung einer Immobilie gelockt werden.
Auf der Rückseite soll es so sein, dass Kunden ankreuzen können, ob Sie eine Immobilie evtl. Verkaufen möchten und eine kostenlose Bewertung wünschen.
Evtl. macht es Sinn zwei Karten anzulegen. Einmal Zielgruppe Käufer/Suchende, einmal Verkäufer.
Beim Format bin ich flexibel und für alles . Es kann länglich sein, aber auch quadratisch.
Vom Design einen Bezug zu den bisherigen Flyern und Broschüren im Anhang.
Bilder die auf der Homepage sind, sind als Stockbilder vorhanden.
Es werden noch einige andere Sachen für das Stadtfest benötigt. Wie Bierdeckel, Imagebroschüre zum Aufklappen, Banner, Roll-Up, Luftballons.

```html
<!DOCTYPE html>
<html lang="de">
<head>
<meta charset="utf-8">
<title>Harlan Immobilien – Gutscheinkarte</title>
<link href="https://fonts.googleapis.com/css2?family=Ubuntu:wght@400;500;700&family=Cormorant+Garamond:wght@500&display=swap" rel="stylesheet">
<style>
:root{
  --navy:#23396b;
  --gold:#c7ad5a;
  --gold-light:#e2d6a8;
  --paper:#fdfcf9;
  --stage:#666666;
  --ink:#4a4a4a;
}
*{margin:0;padding:0;box-sizing:border-box}
html,body{width:959px;height:1200px;overflow:hidden;background:var(--stage)}
body{position:relative;font-family:'Ubuntu',sans-serif}
.card{position:absolute;left:60px;width:839px;height:512px;background:var(--paper);overflow:hidden}
.card--front{top:71px}
.card--back{top:618px;height:511px}
.abs{position:absolute}

/* front */
.photo-family{left:0;top:0;width:514px;height:512px;
  background:linear-gradient(135deg,#f3e6d2 0%,#e3c7a3 35%,#b98559 65%,#6e4a33 100%)}
.panel-right{left:514px;top:0;width:295px;height:512px;background:linear-gradient(180deg,#f7f3ee,#efe9e2)}
.strip-gold{left:809px;top:0;width:30px;height:512px;background:var(--gold-light)}
.strip-gold-dark{left:809px;top:276px;width:30px;height:149px;background:var(--gold)}
.brand-mark{left:607px;top:47px;width:110px;height:110px;background:var(--gold);outline:1px solid var(--gold);outline-offset:6px}
.brand-name{left:514px;width:295px;text-align:center;color:var(--navy);font-family:'Cormorant Garamond',serif;font-weight:500}
.brand-name--big{top:172px;font-size:52px;letter-spacing:6px;line-height:1}
.brand-name--small{top:233px;font-size:13px;letter-spacing:3px}
.voucher-box{left:396px;top:276px;width:401px;height:149px;background:var(--navy)}
.frame{border:1px solid #fff}
.frame-outer{left:381px;top:262px;width:422px;height:177px}
.frame-inner{left:386px;top:267px;width:412px;height:167px}
.voucher-title{left:396px;top:290px;width:382px;text-align:right;color:#fff;font-weight:700;font-size:58px;line-height:1;letter-spacing:-1px}
.voucher-sub{left:396px;top:353px;width:382px;text-align:right;color:var(--gold);font-weight:700;font-size:21px;line-height:26px}
.call-line{left:514px;top:446px;width:267px;text-align:right;color:var(--gold);font-weight:500;font-size:13px}
.phone{left:514px;top:463px;width:267px;text-align:right;color:var(--navy);font-weight:700;font-size:28px;line-height:34px}
.phone-icon{left:529px;top:471px}

/* back */
.photo-house{left:30px;top:0;width:809px;height:285px;
  background:linear-gradient(90deg,#2c3a55 0%,#5b6a80 40%,#b5b8bd 65%,#6f8b6a 100%)}
.back-strip{left:0;top:0;width:30px;height:511px;background:var(--gold-light)}
.back-strip-dark{left:0;top:58px;width:30px;height:245px;background:var(--gold)}
.back-strip-photo{left:0;top:0;width:30px;height:58px;background:#a7a37a}
.question-box{left:30px;top:58px;width:399px;height:245px;background:rgba(35,57,107,.93)}
.frame-gold{border:1px solid #d7c58d}
.frame-back-outer{left:37px;top:42px;width:411px;height:282px}
.frame-back-inner{left:42px;top:47px;width:401px;height:272px}
.question{left:69px;top:78px;color:#fff;font-weight:700;font-size:35px;line-height:40px}
.question-sub{left:69px;top:196px;color:var(--gold);font-weight:700;font-size:17px}
.question-body{left:69px;top:221px;width:350px;color:#fff;font-size:12.5px;line-height:18px}
.cta{left:69px;top:338px;color:var(--gold);font-weight:700;font-size:21px;line-height:25px}
.mini-mark{left:84px;top:402px;width:48px;height:48px;background:var(--gold);outline:1px solid var(--gold);outline-offset:3px}
.mini-name{left:66px;width:85px;text-align:center;color:var(--navy);font-family:'Cormorant Garamond',serif;font-weight:500}
.mini-name--big{top:458px;font-size:22px;letter-spacing:2px;line-height:1}
.mini-name--small{top:480px;font-size:6px;letter-spacing:1px}
.contact{left:170px;top:400px;color:#555;font-size:12.5px;line-height:14.5px}
.contact strong{font-weight:700;color:#555}
.contact p+p{margin-top:15px}
.form-label{color:#666;font-weight:700;font-size:12.5px}
.checkbox{width:23px;height:23px;border:2px solid var(--gold);border-radius:5px}
.form-line{left:481px;width:313px;height:2px;background:var(--gold)}
</style>
</head>
<body>

<section class="card card--front">
  <div class="abs photo-family" role="img" aria-label="Foto: Familie mit Großeltern und Kind beim gemeinsamen Essen am Holztisch in heller Wohnung"></div>
  <div class="abs panel-right"></div>
  <div class="abs strip-gold"></div>
  <div class="abs strip-gold-dark"></div>

  <div class="abs brand-mark"></div>
  <div class="abs brand-name brand-name--big">HARLAN</div>
  <div class="abs brand-name brand-name--small">IMMOBILIEN</div>

  <div class="abs voucher-box"></div>
  <div class="abs frame frame-outer"></div>
  <div class="abs frame frame-inner"></div>
  <h1 class="abs voucher-title">GUTSCHEIN</h1>
  <p class="abs voucher-sub">eine unverbindliche kostenfreie<br>Bewertung Ihrer Immobilie.</p>

  <p class="abs call-line">Wir freuen uns auf Ihren Anruf!</p>
  <svg class="abs phone-icon" width="22" height="22" viewBox="0 0 24 24" aria-hidden="true"><path fill="#c7ad5a" d="M6.6 10.8a15.1 15.1 0 0 0 6.6 6.6l2.2-2.2a1 1 0 0 1 1-.25 11.4 11.4 0 0 0 3.6.57 1 1 0 0 1 1 1V20a1 1 0 0 1-1 1A17 17 0 0 1 3 4a1 1 0 0 1 1-1h3.5a1 1 0 0 1 1 1c0 1.25.2 2.45.57 3.57a1 1 0 0 1-.25 1z"/></svg>
  <p class="abs phone">01234. 56 78 900</p>
</section>

<section class="card card--back">
  <div class="abs photo-house" role="img" aria-label="Foto: modernes Einfamilienhaus mit Doppelgarage und Nadelbäumen in der Abenddämmerung"></div>
  <div class="abs back-strip"></div>
  <div class="abs back-strip-photo"></div>
  <div class="abs back-strip-dark"></div>

  <div class="abs question-box"></div>
  <div class="abs frame-gold frame-back-outer"></div>
  <div class="abs frame-gold frame-back-inner"></div>
  <h2 class="abs question">WIEVIEL IST<br>MEINE IMMOBILIE<br>EIGENTLICH WERT?</h2>
  <p class="abs question-sub">Unsere Leidenschaft für Ihre Immobilie.</p>
  <p class="abs question-body">Sollten auch Sie mit dem Gedanken spielen, sich wohnlich zu verändern, so beraten wir Sie gerne persönlich In einem unverbindlichen Gespräch.</p>

  <h3 class="abs cta">KONTAKTIEREN SIE UNS FÜR<br>EINE KOSTENLOSE BEWERTUNG</h3>

  <div class="abs mini-mark"></div>
  <div class="abs mini-name mini-name--big">HARLAN</div>
  <div class="abs mini-name mini-name--small">IMMOBILIEN</div>

  <div class="abs contact">
    <p><strong>HARLAN IMMOBILIEN – seit 2009</strong><br>Ihre Maklerin in Talbach und Umgebung<br>info@harlanimmobilien.de | harlanimmobilien.de</p>
    <p>Miriam Harlan | Kauffrau der Grundstücks-<br>und Wohnungswirtschaft (IHK)</p>
  </div>

  <span class="abs form-label" style="left:481px;top:319px">ob Sie eine Beratung</span>
  <div class="abs checkbox" style="left:624px;top:315px"></div>
  <span class="abs form-label" style="left:656px;top:320px">VON</span>
  <div class="abs checkbox" style="left:708px;top:315px"></div>
  <span class="abs form-label" style="left:741px;top:320px">NEIN</span>

  <span class="abs form-label" style="left:481px;top:358px">Bewertung Ihrer Immobilie</span>
  <div class="abs form-line" style="top:404px"></div>
  <span class="abs form-label" style="left:481px;top:429px">Kontaktdaten</span>
  <div class="abs form-line" style="top:473px"></div>
</section>

</body>
</html>
```